Letterhead Design Project

Letterhead for a Consultant Cardiologist in Adelaide Australia. Should be very classy, mature and imposing. I would prefer colours that portray confidence, gentleness and serenity.

The PDF attached is for you to see the details that will be on the letterhead and not the design which is extremely poor!

Target Market(s)

Health professionals especially medical doctors

Industry/Entity Type

Consultant

```html
<!DOCTYPE html>
<html lang="en">
<head>
<meta charset="utf-8">
<title>Letterhead – Dr Adaeze M. Okonkwo, Cardiologist</title>
<link rel="stylesheet" href="https://fonts.googleapis.com/css2?family=Arimo:wght@400;700&display=swap">
<style>
  :root {
    --paper: #ffffff;
    --ink: #2b2b2b;
    --accent: #d7202b;
    --rule: #9a9a9a;
  }
  * { margin: 0; padding: 0; box-sizing: border-box; }
  html, body { width: 1063px; height: 1200px; overflow: hidden; background: var(--paper); }
  body { font-family: "Arimo", Arial, sans-serif; color: var(--ink); }
  .letterhead { position: relative; width: 1063px; height: 1200px; background: var(--paper); }

  .brand-mark {
    position: absolute; left: 46px; top: 58px;
    width: 58px; height: 58px; border-radius: 50%;
    background: var(--accent);
  }
  .doctor-name {
    position: absolute; left: 233px; top: 62px;
    font-size: 26px; font-weight: 400; letter-spacing: 0.2px; white-space: nowrap;
  }
  .specialty {
    position: absolute; left: 673px; top: 62px;
    font-size: 26px; color: var(--accent); white-space: nowrap;
  }
  .header-rule {
    position: absolute; left: 175px; top: 93px; width: 840px; height: 2px;
    background: var(--accent);
  }
  .qualifications {
    position: absolute; left: 233px; top: 98px;
    font-size: 13px; letter-spacing: 0.3px;
  }

  .footer-label {
    position: absolute; left: 29px; top: 1040px;
    font-size: 18px;
  }
  .divider {
    position: absolute; top: 1027px; width: 1px; height: 146px;
    background: var(--rule);
  }
  .location {
    position: absolute; top: 1040px;
    font-size: 13px; line-height: 15.5px; white-space: nowrap;
  }
  .location h3 { font-size: 13.5px; font-weight: 700; color: var(--accent); line-height: 16px; margin-bottom: 1px; }
  .location .label { color: var(--accent); }
</style>
</head>
<body>
<div class="letterhead">
  <header>
    <span class="brand-mark" aria-hidden="true"></span>
    <h1 class="doctor-name">Dr&nbsp; Adaeze. M. Okonkwo</h1>
    <p class="specialty">Cardiologist</p>
    <div class="header-rule"></div>
    <p class="qualifications">M.B.B.S, F.M.C.P, F.R.A.C.P</p>
  </header>

  <footer>
    <p class="footer-label">Consulting</p>

    <div class="divider" style="left:171px"></div>
    <div class="location" style="left:218px">
      <h3>The Linden Specialist Centre</h3>
      <p>48 Marlow Road</p>
      <p>Marlow South SA 5019</p>
      <p><span class="label">T:</span> 8355 2170</p>
      <p><span class="label">F:</span> 8355 2188</p>
      <p><span class="label">Provider No:</span>&nbsp; 518264LT</p>
    </div>

    <div class="divider" style="left:451px"></div>
    <div class="location" style="left:496px">
      <h3>Northern Heart &amp; Specialist Clinic</h3>
      <p>St Brennan Central Districts</p>
      <p>Private Hospital</p>
      <p>14-20 Alder Road</p>
      <p>Brookvale SA 5114</p>
      <p><span class="label">T:</span>&nbsp; 8361 4020</p>
      <p><span class="label">F:</span>&nbsp; 8361 4029</p>
      <p><span class="label">E:</span>&nbsp; heart@nhsclinic.com.au</p>
      <p><span class="label">Provider No:</span>&nbsp; 518264KN</p>
    </div>

    <div class="divider" style="left:832px"></div>
    <div class="location" style="left:870px">
      <h3>Port Weston Hospital</h3>
      <p>62 Harbour Road</p>
      <p>Port Weston 5703</p>
      <p><span class="label">T</span>&nbsp; 8672 3300</p>
      <p><span class="label">F:</span> 8355 2188</p>
      <p><span class="label">Provider No:</span> 518264WR</p>
    </div>
  </footer>
</div>
</body>
</html>
```